New CV / Resume for CIO / Head IT

I would need a new fresh design for my CV, which reflects the seniority of a CIO but also looks fresh, has some IT / digital connection.

What I need...
- CV / Resume
- Cover Letter
- ProfilNetz Background
- Logo / Business Card Design

Old CV is attached (do not include latest position) and ProfilNetz Profile could be looked at https://www.profilnetz.example/in/morbekjulian/

Please do not reuse the old design elements. I really want a new design like the ones below. Some good examples
https://vorlagenhalle.example/PaleStudio/5583014-Modern-Resume-Template?u=kzt
https://vorlagenhalle.example/quorvendale/331207-ResumeCV?u=kzt

Target Market(s)

IT

Font styles to use
Serif
Sans Serif

Colors
0094D4
00A9DD
6FCCEA
C7EBF8
E9F6FB

```html
<!DOCTYPE html>
<html lang="en">
<head>
<meta charset="utf-8">
<title>Resume Template — Julian Morbek</title>
<link rel="stylesheet" href="https://fonts.googleapis.com/css2?family=Oswald:wght@500;600&family=Poppins:wght@300;400;500;600;700&display=swap">
<style>
:root{
  --blue:#0094D4;
  --blue-mid:#3A7FD0;
  --sky:#00A9DD;
  --sky-light:#8FD8EE;
  --ice:#C7EBF8;
  --ink:#1d1d1f;
  --text:#4a4a4a;
  --muted:#7a7a7a;
  --sheet:#ffffff;
  --canvas:#ffffff;
  --red:#ee1c1c;
  --list-blue:#1f8fd8;
}
*{box-sizing:border-box;margin:0;padding:0}
html,body{width:1200px;height:1000px;overflow:hidden;background:var(--canvas)}
body{position:relative;font-family:"Poppins",sans-serif;color:var(--text)}
.sheet{position:absolute;width:341px;height:441px;background:var(--sheet);box-shadow:0 0 6px rgba(0,0,0,.12);overflow:hidden}
.abs{position:absolute}
.sidebar{position:absolute;background:var(--ink);color:#fff}
.side-heading{position:absolute;font-size:6px;color:var(--sky);font-weight:400}
.side-text{position:absolute;font-size:5px;line-height:1.5;color:#fff}
.side-text b{font-weight:600;font-size:4.7px;display:block}
.side-rule{position:absolute;height:1px;background:#bbb}
.heading{position:absolute;font-size:6px;color:var(--blue);font-weight:400}
.heading-bar{position:absolute;width:17px;height:1.5px;background:var(--blue)}
.small{font-size:5.2px;line-height:1.6;color:var(--text)}
.date{position:absolute;font-size:5px;color:var(--blue)}
.entry{position:absolute;font-size:5px;line-height:1.3;color:#555}
.entry .org{color:var(--blue)}
.timeline{position:absolute;width:1px;background:var(--blue-mid)}
.dot{position:absolute;width:4px;height:4px;border-radius:50%;background:var(--blue-mid)}
.bullets{position:absolute;list-style:none;font-size:4.5px;line-height:1.55;color:#555}
.bullets li{position:relative;padding-left:9px}
.bullets li::before{content:"";position:absolute;left:0;top:2px;border-left:2.4px solid var(--blue-mid);border-top:1.5px solid transparent;border-bottom:1.5px solid transparent}
.photo{position:absolute;background:linear-gradient(135deg,#e4e4e4,#c9c9c9 55%,#d8d8d8)}
.photo-dark{position:absolute;background:linear-gradient(160deg,#6b6b6b,#2e2e2e)}
.name{position:absolute;font-family:"Oswald",sans-serif;font-weight:600;color:#fff;letter-spacing:.2px}
.signature-area{position:absolute;background:linear-gradient(90deg,#eef3fb,#f7f9fd)}
.promo-title{position:absolute;left:771px;top:524px;font-size:23.5px;line-height:28.5px;font-weight:700;color:var(--red);letter-spacing:.6px}
.promo-list{position:absolute;left:771px;top:636px;list-style:none;font-size:22px;line-height:26px;font-weight:300;color:var(--list-blue);letter-spacing:.5px}
</style>
</head>
<body>

<!-- Cover letter -->
<section class="sheet" style="left:33px;top:27px">
  <div class="photo" style="left:7px;top:11px;width:327px;height:209px" role="img" aria-label="Portrait of Julian Morbek in a suit over a sketched IT-concepts background"></div>
  <svg class="abs" style="left:7px;top:188px" width="327" height="21" viewBox="0 0 327 21">
    <polygon points="0,0 300,0 327,21 0,21" fill="var(--sky-light)"/>
    <polygon points="0,0 120,0 140,21 0,21" fill="var(--sky)"/>
  </svg>
  <div class="name" style="left:26px;top:189px;font-size:14px">Julian Morbek</div>
  <div class="abs" style="left:146px;top:196px;font-size:8.5px;color:#fff">Head – IT, Manager &amp; Coach</div>

  <div class="abs" style="left:22px;top:236px;font-size:7.5px;color:#222;font-weight:500">Cover Letter</div>
  <p class="abs small" style="left:22px;top:253px;width:295px">Lorem ipsum dolor sit amet, consectetur adipiscing elit. Suspendisse eu venenatis metus. Mauris metus libero, scelerisque vel rutrum sit amet, laoreet nec arcu. Nam facilisis imperdiet sodales. Aliquam luctus tincidunt massa, sed maximus lorem tempus ut. In nec aliquet est.</p>
  <ol class="abs small" style="left:37px;top:291px;width:175px;padding-left:8px">
    <li style="margin-bottom:2px">Agile leadership and coaching experience for globally distributed teams (up to 30 employees)</li>
    <li style="margin-bottom:2px">Profound expertise in project and cost management</li>
    <li>Many years of experience with collaboration infrastructures, engineering, and architecture</li>
  </ol>
  <div class="signature-area" style="left:22px;top:344px;width:60px;height:22px" role="img" aria-label="Handwritten signature"></div>
  <div class="abs" style="left:22px;top:376px;width:57px;height:1px;background:#999"></div>
  <div class="abs small" style="left:22px;top:380px;color:#333">Signature</div>
  <div class="abs" style="left:20px;top:397px;width:307px;height:1px;background:#777"></div>
  <div class="abs" style="left:22px;top:403px;font-size:5.2px;line-height:1.9;color:#333;font-weight:500">
    <div><span style="color:var(--blue)">E:</span> julian.morbek@postfach.example</div>
    <div><span style="color:var(--blue)">P:</span> +41 790004512</div>
    <div>Uferweg 7,</div>
  </div>
</section>

<!-- Resume page 1 -->
<section class="sheet" style="left:398px;top:27px">
  <div class="sidebar" style="left:7px;top:9px;width:106px;height:422px"></div>
  <div class="photo-dark" style="left:7px;top:9px;width:106px;height:64px" role="img" aria-label="Portrait photo of Julian Morbek"></div>
  <svg class="abs" style="left:7px;top:73px" width="327" height="34" viewBox="0 0 327 34">
    <polygon points="0,0 140,0 134,34 0,34" fill="var(--blue-mid)"/>
    <polygon points="122,0 140,0 134,34 104,34" fill="#7ea6e0"/>
    <polygon points="140,0 327,0 327,34 134,34" fill="var(--sky-light)"/>
    <polygon points="128,0 140,0 150,34 140,34" fill="#fff" opacity=".6"/>
  </svg>
  <div class="name" style="left:14px;top:89px;font-size:13px">Julian Morbek</div>
  <div class="abs" style="left:153px;top:89px;font-size:4.8px;line-height:1.9;color:var(--blue)">
    <div>+41 790004512</div>
    <div style="padding-left:7px">julian.morbek@postfach.example</div>
  </div>
  <div class="abs" style="left:163px;top:108px;font-size:4.8px;color:var(--blue)">Uferweg 7, CH-5720 Seedorf am</div>

  <div class="side-heading" style="left:14px;top:119px">Personal Details</div>
  <div class="side-text" style="left:14px;top:135px;width:95px">
    <b>Birthday / Place</b>03.1985 in Tannhausen / Germany
    <b style="margin-top:3px">Nationality</b>German
    <b style="margin-top:3px">Marital Status</b>Married (2017 Seedorf)
    <b style="margin-top:3px">Children</b>2 Girls
  </div>
  <div class="side-rule" style="left:13px;top:220px;width:94px"></div>
  <div class="side-heading" style="left:13px;top:234px">Area Of Expertise</div>
  <div class="side-rule" style="left:13px;top:246px;width:16px;background:#fff"></div>
  <div class="side-text" style="left:13px;top:251px;width:95px">
    Agile Leadership<br>Service Design &amp; Transition<br>Coaching<br>Suite 365
    <div style="height:4px"></div>
    Design &amp; Engineering<br>Project Management<br>Shell Scripting<br>Migration &amp; Architecture
    <div style="height:4px"></div>
    IT Consulting &amp; Support<br>Personnel Training<br>Experience Abroad<br>Change Management
  </div>
  <div class="side-rule" style="left:13px;top:362px;width:97px"></div>
  <div class="side-heading" style="left:15px;top:374px">Language</div>
  <div class="side-rule" style="left:15px;top:384px;width:16px;background:#fff"></div>
  <div class="side-text" style="left:15px;top:389px;width:92px">German native,<br>English- very good written &amp; spoken</div>

  <div class="heading" style="left:123px;top:24px">Introduction</div>
  <p class="abs small" style="left:122px;top:38px;width:196px">[Grab your reader's attention with a great quote from the document or use this space to emphasize a key point. To place this text box anywhere on the page, just drag it.]</p>

  <div class="heading" style="left:124px;top:118px">Education &amp; Vocational Trainings</div>
  <div class="timeline" style="left:182px;top:142px;height:177px"></div>
  <div class="abs" style="left:120px;top:319px;width:204px;height:1px;background:var(--blue-mid)"></div>
  <div class="date" style="left:128px;top:142px">03.2018-06.2018</div>
  <div class="dot" style="left:180px;top:143px"></div>
  <div class="entry" style="left:191px;top:141px;width:130px">Hochschule Nordtal HSN<br><span class="org">Course of Studies: CAS Digital Business Development</span></div>
  <div class="date" style="left:128px;top:168px">08.2017-01.2018</div>
  <div class="dot" style="left:180px;top:169px"></div>
  <div class="entry" style="left:191px;top:167px;width:130px">Hochschule Nordtal HSN<br><span class="org">Course of Studies: CAS Cloud Computing</span></div>
  <div class="date" style="left:128px;top:187px">02.2017-06.2017</div>
  <div class="dot" style="left:180px;top:188px"></div>
  <div class="entry" style="left:191px;top:186px;width:130px">Hochschule Nordtal HSN<br><span class="org">Course of Studies: CAS IT Management</span></div>
  <div class="date" style="left:128px;top:206px">11.2013-12.2016</div>
  <div class="dot" style="left:180px;top:207px"></div>
  <div class="entry" style="left:191px;top:205px;width:132px">Lernwerk Bildung AG<br><span class="org">Course of Studies: Business Engineer with Bachelor's Degree</span><br>Dipl. Wirtschaftsinformatiker HF (equivalent to bachelor's degree)</div>
  <div class="date" style="left:128px;top:244px">09.2003-06.2006</div>
  <div class="dot" style="left:180px;top:245px"></div>
  <div class="entry" style="left:191px;top:243px;width:132px">TechServ GmbH, Tannbach (Germany)<br>Apprenticeship as an Information and Telecommunication Technician<br><span class="org">Certified by the Regional Chamber of Trade and Crafts (RKH)</span></div>
  <div class="date" style="left:128px;top:283px">08.2001-08.2003</div>
  <div class="dot" style="left:180px;top:284px"></div>
  <div class="entry" style="left:191px;top:282px;width:132px">Albrecht Keller Technical High-School, Tannbach (Germany)</div>

  <div class="heading" style="left:124px;top:328px">Professional Experience</div>
  <div class="date" style="left:125px;top:346px">Since 12.2018</div>
  <div class="timeline" style="left:182px;top:346px;height:60px"></div>
  <div class="dot" style="left:180px;top:347px"></div>
  <div class="entry" style="left:189px;top:346px;width:136px">Head IT Hero &amp; Head ICT Cluster Central<br><span class="org">Nordhafen AG / Lindwerk GmbH &amp; Co. KGaA</span></div>
  <ul class="bullets" style="left:191px;top:372px;width:134px">
    <li>Operational and personnel responsibility for the IT organization in Switzerland</li>
    <li>Operational and personnel responsibility for the ICT organization in Germany</li>
    <li>Support of the global export organization and HQ</li>
  </ul>
</section>

<!-- Resume page 2 -->
<section class="sheet" style="left:763px;top:27px">
  <div class="sidebar" style="left:11px;top:9px;width:107px;height:422px"></div>
  <div class="side-heading" style="left:18px;top:27px">IT Skills</div>
  <div class="side-rule" style="left:18px;top:37px;width:17px;background:#fff"></div>
  <div class="side-text" style="left:18px;top:42px;width:96px">
    <b>OPERATING SYSTEMS:</b>WinCore Server &amp; Client
    <b style="margin-top:5px">MIDDLEWARE:</b>TeamPortal 2007 – 2016, DataCore Server, WebHost
    <b style="margin-top:5px">PRODUCTS:</b>TeamPortal 2007 – 2016, Nimbus Cloud, Suite 365, Wordsmith Office, Wordsmith Project, Vaultline Backup, Flowgrid Forms, GovernDesk, ShowMe Portal, Lexora 7
    <b style="margin-top:5px">SCRIPTING:</b>CoreShell, Config-as-Code, Batch<br>Tools: CodeStudio, Shell GUI, Scriptworks Studio, DiffView
    <b style="margin-top:5px">ADDITIONAL TECHNOLOGIES:</b>DirectoryHub, DNS, GPO, VPN, GateGuard Server, Network Load Balancing, WinCore / DB clustering
  </div>
  <div class="side-rule" style="left:18px;top:242px;width:94px"></div>
  <div class="side-heading" style="left:18px;top:258px">Genral Information</div>
  <div class="side-rule" style="left:18px;top:268px;width:17px;background:#fff"></div>
  <div class="side-text" style="left:18px;top:273px;width:92px">
    <b>DRIVERS LICENSE:</b>German Class B (Full, Clean license)
    <b style="margin-top:5px">HONORARY OFFICE:</b>Expert member of the examination board PK19 for informatics professionals
    <b style="margin-top:10px">HOBBIES &amp; INTERESTS:</b>Travelling &amp; forein cultures, electrical engineering, Blockchain (mining), sailing, destructive technologies
  </div>

  <div class="heading" style="left:128px;top:27px">Professional Experience - contd..</div>
  <div class="heading-bar" style="left:128px;top:38px"></div>
  <div class="timeline" style="left:187px;top:47px;height:377px"></div>
  <div class="dot" style="left:185px;top:46px"></div>
  <ul class="bullets" style="left:203px;top:45px;width:128px">
    <li>Planning, organization and development of IT infrastructure and application</li>
    <li>Operation of the Service Desk Organization in Switzerland &amp; Germany</li>
    <li>Coordination and implementation with the Group IT strategy</li>
    <li>IT Change and Project Management</li>
  </ul>
  <div class="date" style="left:132px;top:107px">07.2017 - 11.2018</div>
  <div class="entry" style="left:196px;top:106px;width:135px">Manager and Coach of DWP Platform Engineering &amp; Operations<br><span class="org">Alpina Re Management Ltd (Switzerland)</span></div>
  <ul class="bullets" style="left:203px;top:132px;width:128px">
    <li>People management for 31 employees (MBO, hiring, escalations, etc.)</li>
    <li>Personal development coaching (systemic)</li>
    <li>Drive change management and cultural development</li>
    <li>Organization transformation to adopt agile principles</li>
    <li>Shape and support the Digital Workplace strategy</li>
    <li>Support sourcing activities</li>
    <li>Drive and support the strategic planning of our global platforms</li>
    <li>(MailHub, TeamPortal &amp; Talkline / UC)</li>
  </ul>
  <div class="date" style="left:132px;top:228px">05.2014 – 06.2017</div>
  <div class="entry" style="left:196px;top:227px;width:135px">Expert TeamPortal Engineer &amp; Project Manager<br><span class="org">Alpina Re Management Ltd (Switzerland)</span></div>
  <div class="dot" style="left:185px;top:250px"></div>
  <ul class="bullets" style="left:203px;top:247px;width:128px">
    <li>Project Manager of the TeamPortal 2016 &amp; Hybrid project</li>
    <li>Defining and Engineering Suite 365 / TeamPortal online implementation</li>
    <li>Technical responsibility for the TeamPortal infrastructure</li>
    <li>Project lead for TeamPortal 2016 migration and the preparation of an Suite 365-based hybrid solution</li>
    <li>Support and consulting for introduction projects for Business Intelligence, TeamPortal for mobile devices, taxonomy and access management during development and implementation phases</li>
    <li>Level 4 support and problem management for the TeamPortal infrastructure</li>
    <li>Execution of a TeamPortal Risk Assessment RA+</li>
    <li>Engineering and implementation of need-to-protect solution for personal sensitive data on TeamPortal via CoreShell automation</li>
    <li>Harmonization of CoreShell scripts and introduction of script logging and error handling functionality</li>
  </ul>
</section>

<!-- Resume page 3 -->
<section class="sheet" style="left:33px;top:491px">
  <div class="sidebar" style="left:7px;top:10px;width:107px;height:422px"></div>
  <div class="side-heading" style="left:14px;top:24px">Certification</div>
  <div class="side-rule" style="left:14px;top:34px;width:17px;background:#fff"></div>
  <div class="side-text" style="left:14px;top:39px;width:96px;line-height:1.45">
    <div style="margin-bottom:3.5px">Agile Leader L1 - Certified Agile Leadership</div>
    <div style="margin-bottom:3.5px">Changewise - Change Management</div>
    <div style="margin-bottom:3.5px">WCSE: Productivity / TeamPortal 2016, DataCert Big Data Foundation</div>
    <div style="margin-bottom:3.5px">Delivery Ops Foundation</div>
    <div style="margin-bottom:3.5px">ReqBoard Requirements Engineering Foundation Level, TestBoard Certified Tester Foundation</div>
    <div style="margin-bottom:3.5px">PMQ Level D CertaLink Secure Cloud Services integrator</div>
    <div style="margin-bottom:3.5px">CertaLink Agile Scrum Foundation</div>
    <div style="margin-bottom:3.5px">ServiceFrame v3 Foundation</div>
    <div style="margin-bottom:3.5px">WCSA 2008</div>
    <div style="margin-bottom:3.5px">WCSA Suite 365</div>
    <div style="margin-bottom:3.5px">WCSA WinCore Server 2012 R2</div>
    <div style="margin-bottom:3.5px">WCSE 2003 + Security</div>
    <div style="margin-bottom:3.5px">WCTS TeamPortal Server 2007 / 2010 / 2013</div>
    <div>OpenKernel Junior Level Administrator OKC [1]</div>
  </div>

  <div class="heading" style="left:125px;top:24px">Professional Experience - contd..</div>
  <div class="heading-bar" style="left:125px;top:35px"></div>
  <div class="timeline" style="left:184px;top:43px;height:386px"></div>
  <svg class="abs" style="left:181px;top:40px" width="7" height="7"><polygon points="0,0 7,0 3.5,6" fill="var(--blue-mid)"/></svg>
  <svg class="abs" style="left:181px;top:424px" width="7" height="7"><polygon points="0,0 7,0 3.5,6" fill="var(--blue-mid)"/></svg>
  <div class="abs" style="left:330px;top:43px;font-size:4.5px;color:#555">IT</div>
  <ul class="bullets" style="left:196px;top:42px;width:130px">
    <li>Engineering and implementation of need-to-protect solution for personal sensitive data on TeamPortal via CoreShell automation</li>
    <li>Harmonization of CoreShell scripts and introduction of script logging and error handling functionality</li>
    <li>Introduction and documentation of the TeamPortal vulnerability patching process</li>
    <li>Assignment of tasks and planning of resources for TeamPortal within the TeamPortal team</li>
    <li>Design &amp; Build Work Flowcast Lead for a WebHost DotFrame service project.</li>
    <li>Organization and Communication for the TeamPortal 2016 / 2019 Early Access program</li>
  </ul>
  <div class="date" style="left:129px;top:153px">01.2010-04.2014</div>
  <div class="dot" style="left:182px;top:154px"></div>
  <div class="entry" style="left:192px;top:152px;width:140px">TeamPortal System Engineer<br><span class="org">Bank Steinmann &amp; Co. Ltd., Zürich (Switzerland)</span></div>
  <ul class="bullets" style="left:196px;top:173px;width:130px">
    <li>Specialist responsibility for TeamPortal infrastructure</li>
    <li>Engineering, automation, performance optimization and life cycle management of global TeamPortal farms (intranet, application and collaboration platform)</li>
    <li>Technical design and engineering of TeamPortal-based solutions</li>
    <li>Support for collaboration and infrastructure projects in a Wordsmith environment</li>
    <li>Consulting for DotFrame developers and application officers with regard to the optimal usage of TeamPortal</li>
    <li>Assistance with DotFrame configuration and release management</li>
    <li>Responsibility for deploying DotFrame applications in test and production environments</li>
    <li>2nd and 3rd level-Support of the global TeamPortal infrastructure</li>
    <li>Management Reporting</li>
  </ul>
  <div class="date" style="left:129px;top:323px">06.2007 - 12.2009</div>
  <div class="dot" style="left:182px;top:324px"></div>
  <div class="entry" style="left:192px;top:322px;width:140px">IT Consultant<br><span class="org">Kestrel Consult GmbH(Germany)</span></div>
  <ul class="bullets" style="left:196px;top:343px;width:130px">
    <li>Consulting-for key accounts from telecommunication, energy and automotive industries</li>
    <li>Technical realization of a TeamPortal Enterprise Search pilot project</li>
    <li>Setup and maintenance of an infrastructure based on TeamPortal as well as DataCore servers</li>
    <li>Design and creation of an intranet environment TeamPortal 2007</li>
  </ul>
</section>

<!-- Resume page 4 -->
<section class="sheet" style="left:398px;top:491px">
  <div class="sidebar" style="left:13px;top:10px;width:106px;height:422px"></div>
  <div class="heading" style="left:129px;top:25px">Professional Experience - contd..</div>
  <div class="heading-bar" style="left:129px;top:36px"></div>
  <div class="timeline" style="left:188px;top:42px;height:145px"></div>
  <ul class="bullets" style="left:206px;top:40px;width:126px">
    <li>Design and technical realization of several TeamPortal 2007 environments</li>
    <li>Project coordination and documentation, preparation of status meetings and reporting</li>
    <li>Completion of a trainee program as part of the „Systems Engineering Consulting Academy"</li>
  </ul>
  <div class="date" style="left:133px;top:92px;line-height:1.4">09.2006 –<br>02.2007</div>
  <div class="dot" style="left:186px;top:93px"></div>
  <div class="entry" style="left:196px;top:92px;width:135px">Full-time Training as an IT Security Specialist<br><span class="org">Brenner &amp; Holm AG, Talstadt (Germany)</span></div>
  <ul class="bullets" style="left:206px;top:113px;width:126px">
    <li>Design of WinCore-Server 2003-based infrastructures</li>
    <li>Consolidation of network knowledge (routing, RAS, VPN, LB)</li>
    <li>Complex DNS environments (replication, master-slave concept, stubzone)</li>
    <li>Designing and building complex domain-infrastructures (forests, trusts, branch offices etc.)</li>
  </ul>
  <div class="abs" style="left:127px;top:183px;width:202px;height:1px;background:var(--blue-mid)"></div>
  <div class="abs" style="left:126px;top:191px;width:69px;height:1px;background:#555"></div>
  <div class="signature-area" style="left:129px;top:207px;width:56px;height:22px" role="img" aria-label="Handwritten signature"></div>
  <div class="abs" style="left:129px;top:246px;font-size:5.8px;color:var(--blue);font-weight:500">Julian Morbek</div>
</section>

<!-- Deliverables -->
<h1 class="promo-title">100% Editable Wordsmith<br>Writer Resume Template<br>Final Delivetables:</h1>
<ol class="promo-list">
  <li>1. Wordsmith Writer Doc</li>
  <li>2. Wordsmith Writer Template</li>
  <li>3. PDF file</li>
  <li>4. Separate cover and profile<br>images</li>
</ol>

</body>
</html>
```